business card for a shoe shop

we would like a business card for a family owned shoe shop.
With this information included.
Darnell's Shoe Store
Family owned since 1947

then on other side
Darnell's Shoe Store
Footwear fitting specialist
Phone: 9187 2630
218 Quarry St, Fernleigh Downs 3187
(cnr. Hartwick Rd and Quarry St)
darnellshoes218@examplemail.com
if could incorporate the purple color on card i have attached.

```html
<!DOCTYPE html>
<html lang="en">
<head>
<meta charset="utf-8">
<title>Darnell's Shoe Store – Business Card</title>
<link href="https://fonts.googleapis.com/css2?family=Montserrat:wght@300;400;600&display=swap" rel="stylesheet">
<style>
  :root {
    --backdrop: #dadac3;
    --card: #ffffff;
    --purple: #76539e;
    --grey: #6b6b6b;
    --rule: #7a7a7a;
  }
  html, body {
    margin: 0;
    width: 1200px;
    height: 1200px;
    overflow: hidden;
    background: var(--backdrop);
  }
  .canvas {
    position: relative;
    width: 1200px;
    height: 1200px;
  }
  .card {
    position: absolute;
    left: 345px;
    width: 510px;
    height: 312px;
    background: var(--card);
  }
  .card--front { top: 202px; }
  .card--back  { top: 686px; }

  /* Front face */
  .front-name {
    position: absolute;
    left: 0;
    right: 0;
    top: 112px;
    margin: 0;
    text-align: center;
    font-family: "Montserrat", sans-serif;
    font-weight: 600;
    color: var(--purple);
    font-size: 34px;
    line-height: 42px;
  }
  .front-tagline {
    position: absolute;
    left: 0;
    right: 0;
    top: 170px;
    margin: 0;
    text-align: center;
    font-family: "Montserrat", sans-serif;
    font-weight: 600;
    color: var(--grey);
    font-size: 16px;
    line-height: 23px;
    letter-spacing: 0.5px;
    text-transform: uppercase;
  }

  /* Back face */
  .back-name {
    position: absolute;
    left: 39px;
    top: 50px;
    margin: 0;
    font-family: "Montserrat", sans-serif;
    font-weight: 600;
    color: var(--purple);
    font-size: 25px;
    line-height: 33px;
  }
  .back-divider {
    position: absolute;
    left: 216px;
    top: 34px;
    width: 1.5px;
    height: 102px;
    background: var(--rule);
  }
  .back-specialty {
    position: absolute;
    left: 234px;
    top: 44px;
    margin: 0;
    font-family: "Montserrat", sans-serif;
    font-weight: 300;
    color: var(--grey);
    font-size: 21px;
    line-height: 27px;
    letter-spacing: 0.8px;
    text-transform: uppercase;
  }
  .contact-list {
    list-style: none;
    margin: 0;
    padding: 0;
  }
  .contact-item {
    position: absolute;
    right: 77px;
    text-align: right;
    font-family: "Montserrat", sans-serif;
    font-weight: 400;
    color: var(--purple);
    font-size: 18px;
    line-height: 29px;
    white-space: nowrap;
  }
  .contact-item--phone   { top: 153px; }
  .contact-item--address { top: 189px; }
  .contact-item--email   { top: 254px; }
  .contact-icon {
    position: absolute;
    left: 448px;
    width: 22px;
    height: 22px;
  }
  .contact-icon--phone   { top: 156px; }
  .contact-icon--address { top: 206px; }
  .contact-icon--email   { top: 257px; }
</style>
</head>
<body>
<main class="canvas">

  <section class="card card--front" aria-label="Business card front">
    <h1 class="front-name">Darnell's Shoe Store</h1>
    <p class="front-tagline">Family owned<br>since 1947</p>
  </section>

  <section class="card card--back" aria-label="Business card back">
    <h2 class="back-name">Darnell's<br>Shoe Store</h2>
    <div class="back-divider"></div>
    <p class="back-specialty">Footwear<br>fitting<br>specialist</p>

    <ul class="contact-list">
      <li class="contact-item contact-item--phone">9187 2630</li>
      <li class="contact-item contact-item--address">218 Quarry St, Fernleigh Downs 3187<br>(cnr. Hartwick Rd and Quarry St)</li>
      <li class="contact-item contact-item--email">darnellshoes218@examplemail.com</li>
    </ul>

    <svg class="contact-icon contact-icon--phone" viewBox="0 0 22 22" aria-hidden="true">
      <circle cx="11" cy="11" r="10" fill="none" stroke="#76539e" stroke-width="1.5"/>
      <path d="M7.6 6.2c.5-.4 1-.3 1.3.2l.9 1.5c.2.4.1.8-.2 1.1l-.6.5c.5 1.2 1.4 2.1 2.6 2.7l.5-.6c.3-.3.7-.4 1.1-.2l1.5.9c.5.3.6.8.2 1.3l-.6.7c-.5.5-1.3.7-2 .4-2.6-1-4.4-2.9-5.4-5.4-.3-.7-.1-1.5.4-2z" fill="none" stroke="#76539e" stroke-width="1.2" stroke-linejoin="round"/>
    </svg>

    <svg class="contact-icon contact-icon--address" viewBox="0 0 22 22" aria-hidden="true">
      <circle cx="11" cy="11" r="10" fill="none" stroke="#76539e" stroke-width="1.5"/>
      <path d="M11 16.5s-3.8-4-3.8-6.6a3.8 3.8 0 0 1 7.6 0c0 2.6-3.8 6.6-3.8 6.6z" fill="none" stroke="#76539e" stroke-width="1.3"/>
      <circle cx="11" cy="9.9" r="1.3" fill="#76539e"/>
    </svg>

    <svg class="contact-icon contact-icon--email" viewBox="0 0 22 22" aria-hidden="true">
      <circle cx="11" cy="11" r="10" fill="none" stroke="#76539e" stroke-width="1.5"/>
      <rect x="6.3" y="7.6" width="9.4" height="6.8" rx="0.8" fill="none" stroke="#76539e" stroke-width="1.2"/>
      <path d="M6.6 8l4.4 3.5L15.4 8M6.6 14l3.2-2.8M15.4 14l-3.2-2.8" fill="none" stroke="#76539e" stroke-width="1.1"/>
    </svg>
  </section>

</main>
</body>
</html>
```